Flyer for Aluminium recycling business

We are a startup aluminium recycling business. We don’t have a logo yet. I’ve attached a flyer created by one of our sales people but it’s a bit average and we need something a bit more modern and slick. You have creative license to completely change everything - as long as the information being communicated is the same.

Target Market(s)

Hospitality, Hotels, Apartment blocks, malls etcs

Industry/Entity Type

Aluminium recycling

Requirements
Must have
• the wording
Nice to have
• you have free license on design aspect

```html
<!DOCTYPE html>
<html lang="en">
<head>
<meta charset="utf-8">
<title>Circlewise Metals – Aluminium Recycling Flyer</title>
<link rel="stylesheet" href="https://fonts.googleapis.com/css2?family=Montserrat:wght@600;700;800&family=Roboto+Condensed:wght@300;400;700&family=Libre+Baskerville:ital@1&display=swap">
<style>
  :root {
    --teal: #1fa38c;
    --paper: #ffffff;
    --ink: #231f20;
    --grey: #5a585b;
    --highlight: #fff200;
    --can-silver: #b9b6b2;
    --bin-green: #35a83c;
  }
  * { box-sizing: border-box; margin: 0; padding: 0; }
  html, body { width: 849px; height: 1200px; overflow: hidden; background: var(--paper); }
  .flyer {
    position: relative; width: 849px; height: 1200px;
    background: var(--paper); border: 1px solid #cfcfcf;
    font-family: "Roboto Condensed", Arial, sans-serif; color: var(--ink);
  }
  .sheet { position: absolute; left: 44px; top: 63px; width: 760px; height: 1088px; background: var(--teal); overflow: hidden; }
  .hero-art { position: absolute; left: 0; top: 0; }

  .title-card {
    position: absolute; left: 67px; top: 80px; width: 392px; height: 256px;
    background: var(--paper); transform: rotate(-9.4deg);
    box-shadow: 0 6px 14px rgba(0,0,0,.25);
    font-family: "Montserrat", Arial, sans-serif; padding: 44px 0 0 34px; line-height: 1;
  }
  .title-card .kicker { font-weight: 700; font-size: 25px; color: var(--grey); margin-left: 12px; }
  .title-card .metal { font-weight: 800; font-size: 50px; color: var(--ink); margin-top: 4px; letter-spacing: 0.5px; }
  .title-card .game { font-weight: 700; font-size: 35px; color: var(--grey); margin-top: 6px; margin-left: 8px; }
  .title-card .good-line { display: flex; align-items: baseline; gap: 12px; }
  .title-card .for { font-family: "Libre Baskerville", Georgia, serif; font-style: italic; font-size: 44px; color: var(--grey); }
  .title-card .good { font-weight: 800; font-size: 74px; color: var(--ink); }

  .pledge {
    position: absolute; left: 316px; top: 316px; width: 400px; height: 200px;
    transform: rotate(-9.7deg); transform-origin: center;
  }
  .pledge .bracket { position: absolute; top: 0; width: 26px; height: 200px; border: 3px solid var(--paper); }
  .pledge .bracket.open { left: -6px; border-right: none; }
  .pledge .bracket.close { right: -18px; border-left: none; }
  .pledge p { font-weight: 300; font-size: 31px; line-height: 33px; color: var(--paper); padding: 14px 0 0 24px; white-space: nowrap; }
  .pledge mark { background: var(--highlight); color: var(--ink); padding: 0 2px; font-weight: 400; }
  .pledge .tomorrow { display: block; font-weight: 700; font-size: 37px; letter-spacing: 19px; color: var(--highlight); margin-top: 4px; padding-left: 4px; }

  .brand { position: absolute; left: 71px; top: 455px; display: flex; align-items: center; gap: 12px; }
  .brand .dot { width: 46px; height: 46px; border-radius: 50%; background: var(--bin-green); }
  .brand .name { font-family: "Montserrat", Arial, sans-serif; font-weight: 800; font-size: 20px; line-height: 22px; color: var(--ink); }

  .section-title { position: absolute; color: var(--paper); font-weight: 700; line-height: 1; }
  .simple-title { left: 74px; top: 584px; font-size: 34px; }
  .take-pre { left: 434px; top: 556px; font-size: 21px; }
  .take-title { left: 434px; top: 583px; font-size: 34px; }

  .divider { position: absolute; left: 385px; top: 626px; height: 279px; border-left: 1.5px dotted var(--paper); }

  .step { position: absolute; font-size: 12.5px; line-height: 15px; color: var(--ink); white-space: nowrap; }
  .step.boxed { border: 1.5px solid var(--paper); padding: 0 11px; display: flex; align-items: center; }
  .step.plain { color: var(--paper); }
  .num {
    position: absolute; width: 26px; height: 26px; border-radius: 50%;
    background: var(--ink); color: var(--paper); font-weight: 700; font-size: 19px;
    display: flex; align-items: center; justify-content: center; line-height: 1;
  }

  .contact-band { position: absolute; left: 27px; top: 968px; width: 707px; height: 76px; background: var(--paper); }
  .contact { position: absolute; top: 0; height: 76px; display: flex; align-items: center; gap: 12px; font-size: 17px; color: var(--ink); white-space: nowrap; }
  .contact.phone { left: 43px; }
  .contact.email { left: 450px; }
  .contact .icon { width: 27px; height: 27px; }

  .bin-art { position: absolute; left: 305px; top: 917px; }
</style>
</head>
<body>
<div class="flyer">
  <div class="sheet">
    <svg class="hero-art" width="760" height="330" viewBox="0 0 760 330">
      <defs>
        <linearGradient id="cansTone" x1="0" y1="0" x2="1" y2="1">
          <stop offset="0" stop-color="#a8302b"/>
          <stop offset=".35" stop-color="var(--can-silver)"/>
          <stop offset=".65" stop-color="#c23a33"/>
          <stop offset="1" stop-color="#8f8c88"/>
        </linearGradient>
      </defs>
      <polygon points="0,0 760,0 760,196 0,321" fill="url(#cansTone)" role="img" aria-label="Photo of crushed aluminium drink cans"/>
      <polygon points="0,321 760,196 760,201 0,326" fill="var(--paper)"/>
    </svg>

    <div class="title-card">
      <div class="kicker">Playing The Fair</div>
      <div class="metal">ALUMINIUM</div>
      <div class="game">RECYCLING GAME</div>
      <div class="good-line"><span class="for">for</span><span class="good">GOOD</span></div>
    </div>

    <div class="pledge">
      <span class="bracket open"></span><span class="bracket close"></span>
      <p>Our partnership with you is<br>based on <mark>Common Sense</mark><br><mark>Mutual Gain</mark> and a <mark>Better</mark>
        <span class="tomorrow">TOMORROW</span></p>
    </div>

    <div class="brand">
      <span class="dot"></span>
      <span class="name">CIRCLEWISE<br>METALS</span>
    </div>

    <h2 class="section-title simple-title">It's simple</h2>
    <h3 class="section-title take-pre">Examples of</h3>
    <h2 class="section-title take-title">What we can take</h2>

    <div class="divider"></div>

    <!-- How it works -->
    <div class="step boxed" style="left:72px;top:633px;width:186px;height:40px;">We bring you a free bin</div>
    <span class="num" style="left:223px;top:621px;">1</span>

    <span class="num" style="left:85px;top:698px;">2</span>
    <div class="step plain" style="left:130px;top:675px;">You throw all and any aluminium waste<br>into the bin - no need to super-clean it.<br>Try to compact / squash the aluminium<br>as much as possible.</div>

    <div class="step boxed" style="left:72px;top:750px;width:186px;height:39px;">We collect the bin at no charge</div>
    <span class="num" style="left:223px;top:737px;">3</span>

    <span class="num" style="left:85px;top:797px;">4</span>
    <div class="step plain" style="left:130px;top:795px;">We turn the aluminium waste<br>into a desirable resource</div>

    <div class="step boxed" style="left:72px;top:835px;width:233px;height:71px;padding-left:9px;">We pay you for however much of that<br>resource your waste has generated -<br>and give you a report on that, so you<br>can see how good you are.</div>
    <span class="num" style="left:272px;top:824px;">5</span>

    <!-- Accepted items -->
    <div class="step boxed" style="left:433px;top:634px;width:185px;height:40px;padding-left:15px;">Used beverage cans - any</div>
    <span class="num" style="left:584px;top:622px;">1</span>

    <span class="num" style="left:446px;top:678px;">2</span>
    <div class="step plain" style="left:491px;top:683px;">Tinfoil-scrunched, crusty, burned or dirty</div>

    <div class="step boxed" style="left:433px;top:715px;width:185px;height:34px;">Disposable BBQ roasting trays</div>
    <span class="num" style="left:587px;top:703px;">3</span>

    <span class="num" style="left:446px;top:755px;">4</span>
    <div class="step plain" style="left:491px;top:761px;">Aluminium takeaway containers</div>

    <div class="step boxed" style="left:433px;top:797px;width:232px;height:71px;padding-left:10px;">We pay you for however much of that<br>resource your waste has generated - and<br>give you a report on that, so you can see<br>how good you are.</div>
    <span class="num" style="left:633px;top:788px;">5</span>

    <span class="num" style="left:446px;top:878px;">6</span>
    <div class="step plain" style="left:491px;top:884px;">Tear-off can lids</div>

    <div class="contact-band">
      <div class="contact phone">
        <svg class="icon" viewBox="0 0 28 28" aria-hidden="true">
          <circle cx="14" cy="14" r="14" fill="var(--teal)"/>
          <path d="M9.5 7.5l2.6-.5 1.6 3.6-1.7 1.3c.9 1.8 2.3 3.2 4.1 4.1l1.3-1.7 3.6 1.6-.5 2.6c-.2.8-1 1.3-1.8 1.2C12.8 19 9 15.2 8.3 9.3c-.1-.8.4-1.6 1.2-1.8z" fill="var(--paper)"/>
        </svg>
        <span>021 555 0192</span>
      </div>
      <div class="contact email">
        <svg class="icon" viewBox="0 0 28 28" aria-hidden="true">
          <text x="14" y="23" text-anchor="middle" font-family="Roboto Condensed, Arial, sans-serif" font-size="28" font-weight="700" fill="var(--teal)">@</text>
        </svg>
        <span>hello@circlewisemetals.co.nz</span>
      </div>
    </div>

    <svg class="bin-art" width="145" height="145" viewBox="0 0 145 145">
      <defs>
        <linearGradient id="binTone" x1="0" y1="0" x2="0" y2="1">
          <stop offset="0" stop-color="#9c9a98"/>
          <stop offset=".2" stop-color="var(--bin-green)"/>
          <stop offset="1" stop-color="#238a2b"/>
        </linearGradient>
      </defs>
      <path d="M4 22 H141 L126 141 H19 Z" fill="url(#binTone)" role="img" aria-label="Green recycling bin filled with aluminium cans"/>
    </svg>
  </div>
</div>
</body>
</html>
```